Business Cards

Business cards (double-sided) to be handed out to clients and potential clients, with contact details, logo .

Target Market(s)

Small to medium size businesses

Industry/Entity Type

Accountants

Contact Information for Business Card

Brightwater Ledger & Counsel Ltd

Colors

Designer to choose only greyscale colors for use in the design.

Requirements
Must have
• Name, Title, Address, Phone number, Email, Website
Nice to have
• Modern, clean lines, classy
Should not have
• Business cards to be double-sided. Form keeps reverting to single-sided.

```html
<!DOCTYPE html>
<html lang="en">
<head>
<meta charset="utf-8">
<title>Brightwater Ledger &amp; Counsel – Business Cards</title>
<link rel="stylesheet" href="https://fonts.googleapis.com/css2?family=Montserrat:wght@400;500;700&family=Arimo:wght@400&display=swap">
<style>
  :root {
    --bg: #d4d4d4;
    --card-white: #ffffff;
    --ink: #111111;
    --ink-soft: #2a2a2a;
    --card-black: #1e1e1e;
    --silver: #9a9a9a;
    --on-dark: #ffffff;
  }
  * { margin: 0; padding: 0; box-sizing: border-box; }
  html, body { width: 1200px; height: 800px; overflow: hidden; }
  body {
    background: var(--bg);
    display: flex;
    align-items: center;
    justify-content: center;
    gap: 34px;
  }
  .card {
    position: relative;
    width: 560px;
    height: 320px;
    border-radius: 22px;
    overflow: hidden;
  }
  .card--front { background: var(--card-white); color: var(--ink); }
  .card--back { background: var(--card-black); }

  .corner-block {
    position: absolute;
    top: 0; right: 24px;
    width: 62px; height: 56px;
    background: var(--ink);
  }
  .person {
    position: absolute;
    top: 42px; left: 40px;
    font-family: "Montserrat", sans-serif;
  }
  .person__name { font-weight: 700; font-size: 22px; letter-spacing: 0.2px; }
  .person__title { font-weight: 400; font-size: 14px; letter-spacing: 0.6px; margin-top: 2px; }

  .contact-band {
    position: absolute;
    top: 128px; left: 0;
    width: 290px; height: 100px;
    background: var(--ink);
    color: var(--on-dark);
    padding: 14px 0 0 30px;
    font-family: "Arimo", sans-serif;
    font-size: 14.5px;
    list-style: none;
  }
  .contact-band li { display: flex; align-items: center; gap: 8px; height: 24px; }
  .contact-band svg { width: 14px; height: 14px; flex: none; }

  .address {
    position: absolute;
    top: 252px; left: 150px;
    font-family: "Arimo", sans-serif;
    font-size: 15px;
    line-height: 1.3;
    font-style: normal;
  }

  .brand {
    position: absolute;
    font-family: "Montserrat", sans-serif;
    font-weight: 500;
    letter-spacing: 1.5px;
    text-transform: uppercase;
    display: flex;
    align-items: center;
    gap: 10px;
  }
  .brand__square { width: 12px; height: 12px; flex: none; }
  .card--front .brand { top: 128px; left: 320px; width: 220px; font-size: 17px; line-height: 1.3; color: var(--ink); }
  .card--front .brand__square { background: var(--ink); }
  .card--back .brand { top: 50%; left: 50%; transform: translate(-50%, -50%); font-size: 22px; color: var(--silver); white-space: nowrap; }
  .card--back .brand__square { background: var(--silver); }
</style>
</head>
<body>
  <section class="card card--front" aria-label="Business card front">
    <div class="corner-block"></div>
    <div class="person">
      <p class="person__name">MARCUS HALE</p>
      <p class="person__title">MANAGING DIRECTOR</p>
    </div>
    <ul class="contact-band">
      <li>
        <svg viewBox="0 0 16 16" aria-hidden="true"><circle cx="8" cy="8" r="7.5" fill="#fff"/><path d="M5 4.5l1.5-.5 1 2-1 .8a5 5 0 002.7 2.7l.8-1 2 1-.5 1.5c-3.5.3-6.8-3-6.5-6.5z" fill="#111"/></svg>
        044-987 654 321
      </li>
      <li>
        <svg viewBox="0 0 16 16" aria-hidden="true"><rect x="1" y="3" width="14" height="10" fill="#fff"/><path d="M1 3l7 6 7-6" fill="none" stroke="#111" stroke-width="1.2"/></svg>
        info@brightwaterledger.com
      </li>
      <li>
        <svg viewBox="0 0 16 16" aria-hidden="true"><circle cx="8" cy="8" r="7.5" fill="#fff"/><g fill="none" stroke="#111" stroke-width="1"><circle cx="8" cy="8" r="5.5"/><ellipse cx="8" cy="8" rx="2.3" ry="5.5"/><path d="M2.5 8h11M3.5 5h9M3.5 11h9"/></g></svg>
        www.brightwaterledger.com
      </li>
    </ul>
    <address class="address">17, Harbour Row, Suite 3<br>60218, Country Name</address>
    <div class="brand"><span class="brand__square"></span><span>Brightwater Ledger &amp; Counsel</span></div>
  </section>

  <section class="card card--back" aria-label="Business card back">
    <div class="brand"><span class="brand__square"></span><span>Brightwater Ledger &amp; Counsel</span></div>
  </section>
</body>
</html>
```